Hula-Hoop dance entertainment sales and instruction by twirl-spinette needs a business card

I need a 2 sided business card that is square (although this is not an absolute )for my self employed business as an independent artist. my business name is "Twirl-Spinette" I teach how to hula-hoop classes, make and sell hula-hoops, provided entertainment at kids birthday parties, community events, corporate events and perform at artistic dance shows.
I would like to see spirals or curved lines in the card, and I would like the card to be seen as fun, spunky, flair and eye catching.

the card could double as a tag to go on the hoops i sell,

Target Market(s)

women age 20 - 50

Industry/Entity Type

Entertainment

Requirements
Must have
• Minna Traversi
www.twirlspinette.example
555.734.2619
Nice to have
• I would like my image to be on one side of the card. so people can recognize me!

```html
<!DOCTYPE html>
<html lang="en">
<head>
<meta charset="utf-8">
<title>Twirl-Spinette Business Card</title>
<link rel="stylesheet" href="https://fonts.googleapis.com/css2?family=Dosis:wght@500;600&display=swap">
<style>
  :root {
    --page: #ffffff;
    --card: #ffffff;
    --card-edge: #8a8a8a;
    --pink: #ee6aa7;
    --green: #3cb44a;
    --ink: #333333;
    --figure-a: #f4d3e3;
    --figure-b: #ececec;
  }
  * { margin: 0; padding: 0; box-sizing: border-box; }
  html, body {
    width: 1200px;
    height: 474px;
    overflow: hidden;
    background: var(--page);
  }
  .sheet {
    position: relative;
    width: 1200px;
    height: 474px;
  }
  .card {
    position: absolute;
    top: 86px;
    width: 491px;
    height: 306px;
    background: var(--card);
    border: 1px solid var(--card-edge);
    overflow: hidden;
  }
  .card--front { left: 86px; }
  .card--back { left: 620px; }

  .dancer-figure {
    position: absolute;
    left: 0;
    top: 42px;
    width: 148px;
    height: 236px;
    background: linear-gradient(160deg, var(--figure-b), var(--figure-a));
  }
  .brand-name {
    position: absolute;
    left: 160px;
    top: 130px;
    font-family: "Dosis", sans-serif;
    font-weight: 600;
    font-size: 40px;
    line-height: 1;
    letter-spacing: 0.3px;
    color: var(--pink);
    text-transform: uppercase;
    white-space: nowrap;
  }
  .dash-line {
    position: absolute;
    top: 184px;
    height: 3px;
    background: repeating-linear-gradient(90deg, var(--green) 0 10px, transparent 10px 18px);
  }
  .card--front .dash-line { left: 160px; right: 0; }
  .card--back .dash-line { left: 2px; width: 330px; }

  .owner-name {
    position: absolute;
    left: 0;
    width: 100%;
    top: 136px;
    text-align: center;
    font-family: "Dosis", sans-serif;
    font-weight: 500;
    font-size: 29px;
    line-height: 1;
    color: var(--pink);
  }
  .contact {
    position: absolute;
    left: 0;
    width: 100%;
    top: 206px;
    text-align: center;
    font-family: "Dosis", sans-serif;
    font-weight: 600;
    font-size: 18px;
    line-height: 28px;
    color: var(--ink);
  }
  .contact span { display: block; }
</style>
</head>
<body>
  <main class="sheet">
    <section class="card card--front">
      <div class="dancer-figure" role="img" aria-label="Line drawing of a dancer twirling a pink hula hoop"></div>
      <h1 class="brand-name">Twirl-Spinette</h1>
      <div class="dash-line"></div>
    </section>
    <section class="card card--back">
      <h2 class="owner-name">Minna Traversi</h2>
      <div class="dash-line"></div>
      <p class="contact">
        <span class="contact__phone">555.734.2619</span>
        <span class="contact__web">www.twirlspinette.example</span>
      </p>
    </section>
  </main>
</body>
</html>
```